Email Signature Design

Please design an email signature, the below is an example of our current design;
___

CARRODY ESTATE HOLDINGS PTY LTD
BENEDICT HARLOWE
Licensed Strata and Community Manager

143 Tallowood Street,
KELDARRA NSW 2093

P: 02.9473.6820 F: 9536.2048
Website: www.carrodyestate.com.au

This e-mail message and accompanying data may contain information that is confidential and private. If you are not the intended recipient, the use, dissemination, distribution or copying of this message or data is prohibited.

If you have received this e-mail in error please notify us immediately and delete all material pertaining to this e-mail. strata@carrodyestate.com.au

___

We would like to incorporate our logo and company colours, you can view the colours and feel of image at www.carrodyestate.com.au

Industry/Entity Type

It Company

Requirements
Must have
• use of logo and company colours (image)

```html
<!DOCTYPE html>
<html lang="en">
<head>
<meta charset="utf-8">
<title>Carrody Estate Holdings – Email Signature</title>
<link rel="stylesheet" href="https://fonts.googleapis.com/css2?family=Arimo:wght@400;700&display=swap">
<style>
  :root {
    --olive: #8a7e3a;
    --grey: #6e6e6e;
    --text-grey: #7a7a7a;
    --paper: #ffffff;
  }
  html, body {
    margin: 0;
    padding: 0;
    width: 1200px;
    height: 1000px;
    overflow: hidden;
    background: var(--paper);
    font-family: "Arimo", Arial, sans-serif;
  }
  .signature {
    position: absolute;
    left: 132px;
    top: 290px;
    width: 936px;
  }
  .signer-name {
    margin: 0;
    font-size: 28px;
    font-weight: 700;
    color: var(--olive);
    letter-spacing: 0.5px;
    line-height: 1.1;
  }
  .signer-title {
    margin: 4px 0 0;
    font-size: 21px;
    color: var(--grey);
  }
  .brand {
    position: relative;
    height: 160px;
    margin-top: 42px;
  }
  .brand-square {
    position: absolute;
    left: 0;
    top: 6px;
    width: 146px;
    height: 146px;
    background: var(--olive);
  }
  .brand-text {
    position: absolute;
    left: 240px;
    top: 2px;
  }
  .company-name {
    margin: 0;
    font-size: 40px;
    font-weight: 700;
    color: var(--olive);
    line-height: 1;
    letter-spacing: 0.3px;
  }
  .company-tagline {
    margin: 6px 0 0;
    font-size: 31px;
    color: var(--grey);
    letter-spacing: 0.5px;
    line-height: 1.1;
  }
  .contact {
    display: flex;
    margin-top: 20px;
    font-size: 16px;
    color: var(--text-grey);
    line-height: 1.3;
  }
  .contact-numbers { padding-right: 16px; }
  .contact-address {
    padding-left: 16px;
    border-left: 1px solid var(--text-grey);
  }
  .label, .domain { color: var(--olive); font-weight: 700; }
  .color-band {
    display: flex;
    gap: 3px;
    height: 32px;
    margin-top: 18px;
  }
  .color-band .band-olive { width: 492px; background: var(--olive); }
  .color-band .band-grey { flex: 1; background: var(--grey); }
  .disclaimer {
    margin: 16px 0 0;
    font-size: 15.5px;
    color: var(--text-grey);
    line-height: 1.3;
  }
  .disclaimer + .disclaimer { margin-top: 20px; }
</style>
</head>
<body>
  <section class="signature">
    <h1 class="signer-name">BENEDICT HARLOWE</h1>
    <p class="signer-title">Licensed Strata and Community Manager</p>

    <div class="brand">
      <div class="brand-square"></div>
      <div class="brand-text">
        <p class="company-name">CARRODY ESTATE HOLDINGS</p>
        <p class="company-tagline">STRATA MANAGEMENT SERVICES</p>
        <div class="contact">
          <div class="contact-numbers">
            <span class="label">P:</span> 02.9473.6820 <span class="label">F:</span> 9536.2048<br>
            www.<span class="domain">carrodyestate</span>.com.au
          </div>
          <div class="contact-address">
            143 Tallowood Street,<br>
            KELDARRA NSW 2093
          </div>
        </div>
      </div>
    </div>

    <div class="color-band">
      <div class="band-olive"></div>
      <div class="band-grey"></div>
    </div>

    <p class="disclaimer">This e-mail message and accompanying data may contain information that is confidential and private.<br>
    If you are not the intended recipient, the use, dissemination, distribution or copying of this message or data is prohibited.</p>
    <p class="disclaimer">If you have received this e-mail in error please notify us immediately and delete all material<br>
    pertaining to this e-mail. strata@carrodyestate.com.au</p>
  </section>
</body>
</html>
```